Franchise Power Point

Looking to add a strong design element to a very basic power point presentation about how to find the ideal franchise match. My website is www.brightpathventuring.com and www.vendalink/TKowalczyk

```html
<!DOCTYPE html>
<html lang="en">
<head>
<meta charset="utf-8">
<title>VendaLink – Franchise Presentation Slides</title>
<link rel="stylesheet" href="https://fonts.googleapis.com/css2?family=Montserrat:wght@300;400;500&family=Playfair+Display:wght@700;900&display=swap">
<style>
  :root{
    --page:#f7f7f7;
    --navy:#1d2e47;
    --navy-soft:#25364a;
    --gold:#fcbf14;
    --gold-text:#ffe27f;
    --white:#ffffff;
    --cream:#fbf3ec;
    --photo-warm:#d6a488;
    --ink-grey:#8a8f98;
    --rail:#d8d8d8;
    --serif:'Playfair Display', Georgia, serif;
    --sans:'Montserrat', Arial, sans-serif;
  }
  *{box-sizing:border-box;margin:0;padding:0}
  html,body{width:1200px;height:2728px;overflow:hidden;background:var(--page)}
  .canvas{position:relative;width:1200px;height:2728px}
  .slide{position:absolute;left:118px;width:964px;height:542px;overflow:hidden;
    box-shadow:18px 22px 30px rgba(0,0,0,.28)}
  .slide svg.arc{position:absolute;inset:0}
  .photo-fill{position:absolute;inset:0}
  .footer-band{position:absolute;left:0;right:0;bottom:0;height:22px;
    font:300 10.5px/22px var(--sans);text-align:center;white-space:nowrap}
  .footer-band.gold{background:var(--gold);color:var(--gold-text)}
  .footer-band.navy{background:var(--navy);color:#dfe3ea}

  /* Cover */
  .cover{top:144px;background:var(--navy-soft)}
  .cover .photo-fill{background:#283a4e}
  .cover .brand{position:absolute;top:112px;left:0;right:0;text-align:center;
    font:700 46px/1 var(--serif);color:var(--white)}
  .cover .brand-dot{display:inline-block;width:9px;height:9px;border-radius:50%;
    background:var(--gold);margin-left:6px;vertical-align:middle}
  .cover .tagline{position:absolute;top:172px;left:0;right:0;text-align:center;
    font:400 14px/1 var(--sans);color:#e9ecf1}
  .cover .title{position:absolute;top:295px;left:0;right:0;text-align:center;
    font:700 28px/34px var(--serif);color:var(--white)}
  .cover .rule{position:absolute;top:380px;left:332px;width:300px;height:1px;background:var(--gold)}
  .cover .lede{position:absolute;top:393px;left:90px;right:90px;text-align:center;
    font:400 15.5px/24px var(--sans);color:#dde2ea}
  .cover .social{position:absolute;top:454px;left:0;right:0;display:flex;justify-content:center;gap:15px}
  .cover .social span{width:30px;height:30px;border-radius:50%;background:var(--gold)}

  /* Statement slides */
  .statement-dark{top:776px}
  .statement-light{top:1409px}
  .photo-fill.warm{background:var(--photo-warm)}
  .statement{position:absolute;left:0;text-align:center;font-family:var(--sans);font-weight:300;white-space:nowrap}
  .statement .small{font-size:32px}
  .statement .large{font-size:42px}
  .statement-dark .statement{color:var(--white)}
  .statement-light .statement{color:var(--navy)}
  .underline{position:absolute;height:1px;background:var(--gold)}

  /* Agenda */
  .agenda{top:2041px;background:var(--white)}
  .agenda .portrait{position:absolute;left:0;top:0;width:286px;height:466px;
    background:linear-gradient(160deg,#dfe6ee 0%,#b9c6d6 40%,#2c4577 70%,#1d2f57 100%)}
  .agenda .tab{position:absolute;left:258px;top:127px;width:134px;height:316px;border-radius:10px;
    background:var(--gold);box-shadow:4px 6px 12px rgba(0,0,0,.15)}
  .agenda .tab span{position:absolute;left:50%;top:50%;transform:translate(-50%,-50%) rotate(-90deg);
    font:700 44px/1 var(--serif);color:var(--white);letter-spacing:1px;white-space:nowrap}
  .agenda .brand{position:absolute;right:12px;top:30px;font:700 22px/1 var(--serif);color:var(--navy)}
  .agenda .rail{position:absolute;left:683px;top:144px;width:3px;height:294px;background:var(--rail)}
  .agenda .item{position:absolute;left:0;width:964px;height:0}
  .agenda .node{position:absolute;left:669px;top:-15px;width:30px;height:30px;border-radius:50%;
    border:5px solid var(--gold);background:var(--white)}
  .agenda .label{position:absolute;left:724px;top:-13px;font:400 20px/1.2 var(--sans);color:var(--navy)}
  .agenda .note{position:absolute;right:322px;top:-15px;width:200px;text-align:right;
    font:400 11px/14px var(--sans);color:var(--ink-grey)}
  .agenda .foot{position:absolute;left:0;right:0;bottom:0;height:24px;background:var(--navy);
    border-top:2px solid var(--gold);font:400 11.5px/22px var(--sans);color:#d6dbe3}
  .agenda .foot .copy{position:absolute;left:29px}
  .agenda .foot .page{position:absolute;left:854px}
  .agenda .foot .num{position:absolute;left:906px;padding-left:8px;border-left:2px solid var(--gold)}
</style>
</head>
<body>
<main class="canvas">

  <section class="slide cover">
    <div class="photo-fill" role="img" aria-label="Photo of a person with arms spread wide by the sea, under a dark navy overlay"></div>
    <div class="brand">VendaLink<span class="brand-dot"></span></div>
    <p class="tagline">Helping People Realize Their Dreams</p>
    <h1 class="title">Smart Franchise Decisions Using Logic<br>And Intuition</h1>
    <div class="rule"></div>
    <p class="lede">VendaLink is comprised of dedicated industry experts whose focus is providing the tools and resources needed to make dreams come alive for our candidates.</p>
    <div class="social"><span></span><span></span><span></span><span></span></div>
    <div class="footer-band gold">Copyright © 2023 Harborline Advisory Group - All Rights Reserved</div>
  </section>

  <section class="slide statement-dark">
    <div class="photo-fill warm" role="img" aria-label="Warm-toned photo of a person with arms spread wide by the sea"></div>
    <svg class="arc" width="964" height="542" viewBox="0 0 964 542" aria-hidden="true">
      <circle cx="449" cy="536" r="476" fill="var(--gold)" opacity=".92"/>
      <circle cx="449" cy="536" r="433" fill="var(--navy-soft)" opacity=".94"/>
    </svg>
    <div class="statement" style="top:332px;width:662px"><span class="small">Do not let your</span></div>
    <div class="statement" style="top:368px;width:662px"><span class="large">Entrepreneurial Dream</span> <span class="small">turn</span></div>
    <div class="underline" style="left:65px;top:418px;width:331px"></div>
    <div class="statement" style="top:418px;width:662px"><span class="small" style="font-size:34px">a Technicians Nightmare</span></div>
    <div class="footer-band gold">Copyright © 2023 Harborline Advisory Group - All Rights Reserved</div>
  </section>

  <section class="slide statement-light">
    <div class="photo-fill warm" role="img" aria-label="Warm-toned photo of a person with arms spread wide by the sea"></div>
    <svg class="arc" width="964" height="542" viewBox="0 0 964 542" aria-hidden="true">
      <circle cx="449" cy="536" r="476" fill="var(--gold)" opacity=".92"/>
      <circle cx="449" cy="536" r="433" fill="var(--cream)" opacity=".93"/>
    </svg>
    <div class="statement" style="top:370px;width:602px"><span class="small">Use the</span></div>
    <div class="statement" style="top:415px;width:602px"><span class="large">Educated Approach</span></div>
    <div class="underline" style="left:103px;top:469px;width:388px"></div>
    <div class="footer-band navy">Copyright © 2023 Harborline Advisory Group - All Rights Reserved</div>
  </section>

  <section class="slide agenda">
    <div class="portrait" role="img" aria-label="Portrait photo of a businessman in a navy suit with arms crossed"></div>
    <div class="tab"><span>AGENDA</span></div>
    <div class="brand">VendaLink</div>
    <div class="rail"></div>

    <div class="item" style="top:144px"><p class="note">Lorem ipsum dolor sit amet put<br>any thing here please be it</p><span class="node"></span><span class="label">Our Company</span></div>
    <div class="item" style="top:218px"><p class="note">Lorem ipsum dolor sit amet put<br>any thing here please be i</p><span class="node"></span><span class="label">Our History</span></div>
    <div class="item" style="top:291px"><p class="note">Lorem ipsum dolor sit amet put<br>any thing here please be it</p><span class="node"></span><span class="label">Our Category</span></div>
    <div class="item" style="top:365px"><p class="note">Lorem ipsum dolor sit amet put<br>any thing here please be it</p><span class="node"></span><span class="label">Our Team</span></div>
    <div class="item" style="top:438px"><p class="note">Lorem ipsum dolor sit amet put<br>any thing here please be it</p><span class="node"></span><span class="label">Our Values</span></div>

    <div class="foot">
      <span class="copy">Copyright © 2024 VendaLink- All Rights Reserved.</span>
      <span class="page">Page</span>
      <span class="num">4</span>
    </div>
  </section>

</main>
</body>
</html>
```